Company Flyer for Electric boating company

I am looking for a company flyer which we can hand over to boat owners in the Netherlands (Amsterdam area). Our core business is to rebuild every boat (from 4 to 10 meters) into an electrically propelled boat. We are taking out diesels and replace them with a high quality electrical motor, inboard varying from 30 till 80 pk (hp). And outboard from 1pk (hp) till 200pk. We are the best, not the cheapest, not the most expensive. We only work with the best materials. The flyer has to be sort of in line with our website and branding.

Major advantages of electric boating are:
- completely silent
- no fumes, smells or smoke
- cheap to operate
- environmentally friendly
- obliged in more and more areas
- no maintenance
- more enjoyable

The flyer should be A5 format. Since all the text has to be in Dutch I expect only the graphical design and layout for advantages, process, pricing and contact details etc.

Target Market(s)

Boat owners in the Netherlands

Font styles to use
Sans Serif

Colors
9bcb3c
add136
cadf82
0555a3
3176b5
85acd3
e0ebf3

Requirements
Must have
• Clean design, in line with website: www.volta-kade.nl
Nice to have
• icons for advantages, boating etc

2 sides
Should not have
• Steering wheel...

```html
<!DOCTYPE html>
<html lang="nl">
<head>
<meta charset="utf-8">
<title>Volta Kade – flyer</title>
<link href="https://fonts.googleapis.com/css2?family=Montserrat:wght@400;600;700;800&family=Open+Sans:wght@400;600&display=swap" rel="stylesheet">
<style>
:root{
  --green:#9bcb3c;
  --green-dark:#7fb02a;
  --green-light:#cadf82;
  --ink:#2b2f3d;
  --ink-soft:#3a3f4f;
  --paper:#ffffff;
  --stage:#eceeef;
  --text:#3b3f48;
  --muted:#7a7f88;
  --rule:#d9dce0;
}
*{box-sizing:border-box;margin:0;padding:0}
html,body{width:1200px;height:2244px;overflow:hidden}
body{background:var(--stage);font-family:"Open Sans",Arial,sans-serif;color:var(--text);position:relative}
.page{position:absolute;left:220px;width:760px;height:1075px;background:var(--paper);box-shadow:0 6px 24px rgba(0,0,0,.14);overflow:hidden}
.page--front{top:32px}
.page--back{top:1137px}
h1,h2,h3,h4,.brand{font-family:"Montserrat",Arial,sans-serif}

/* front */
.hero{display:flex;height:300px}
.hero__brand{width:330px;padding:56px 0 0 40px}
.brand{display:flex;align-items:center;gap:14px;font-weight:800;font-size:34px;color:var(--ink);letter-spacing:.5px}
.brand__dot{width:44px;height:44px;border-radius:50%;background:var(--green)}
.brand__sub{font-family:"Montserrat",sans-serif;font-size:11px;letter-spacing:3px;color:var(--muted);margin:6px 0 0 58px;font-weight:600}
.hero__photo{flex:1;background:linear-gradient(160deg,#1e2a33 0%,#4f5b63 45%,#9aa6ad 70%,#2a343c 100%)}
.about-band{position:absolute;top:180px;left:0;width:330px;height:100px;background:var(--green);padding:22px 28px 0 40px;color:#fff}
.about-band h1{font-size:30px;font-weight:800;line-height:1}
.about-band p{font-family:"Montserrat",sans-serif;font-size:11px;letter-spacing:2.5px;margin-top:8px;font-weight:600}
.who{background:var(--ink);color:#fff;display:flex;align-items:center;gap:28px;padding:0 40px;height:62px}
.who h2{font-size:15px;font-weight:700;letter-spacing:1px;white-space:nowrap}
.who p{font-size:11px;line-height:1.5;color:#c9ccd3}
.front-body{display:flex;height:665px}
.benefits{width:300px;background:var(--ink-soft);color:#fff;padding:26px 28px 0 40px;position:relative}
.benefits h2{font-size:17px;font-weight:700;letter-spacing:1px;margin-bottom:18px}
.benefits ul{list-style:none}
.benefits li{display:flex;align-items:center;gap:12px;font-size:12.5px;padding:8px 0;border-bottom:1px solid rgba(255,255,255,.12)}
.benefits svg{flex:none}
.benefits__photo{position:absolute;left:0;right:0;top:380px;height:190px;background:linear-gradient(180deg,#5a6470 0%,#8b4a3f 55%,#2f3640 100%)}
.web-btn{position:absolute;left:40px;right:28px;top:588px;height:44px;background:var(--green);color:#fff;font-family:"Montserrat",sans-serif;font-weight:700;font-size:14px;display:flex;align-items:center;justify-content:center;letter-spacing:.5px}
.pricing{flex:1;padding:26px 40px 0 32px}
.pricing h2{font-size:19px;font-weight:800;color:var(--ink);letter-spacing:.5px}
.pricing__intro{font-size:11px;line-height:1.6;margin:12px 0 18px;color:var(--text)}
.price-block{border-top:1px solid var(--rule);padding:14px 0;display:flex;gap:18px}
.price-block h3{font-size:12px;font-weight:700;color:var(--ink);width:88px;flex:none;line-height:1.35}
.price-block h3 span{display:block;color:var(--green-dark);font-size:10.5px;font-weight:600}
.price-block ul{list-style:none;flex:1;font-size:11px;line-height:1.7}
.price-block li::before{content:"";display:inline-block;width:6px;height:6px;background:var(--green);margin-right:8px;vertical-align:middle}
.price-tag{background:var(--ink);color:#fff;font-family:"Montserrat",sans-serif;font-weight:700;font-size:12px;padding:7px 12px;align-self:flex-start;white-space:nowrap}
.front-foot{position:absolute;bottom:0;left:0;right:0;height:48px;background:var(--ink);display:flex;align-items:center;padding:0 40px;font-size:10.5px;color:#c9ccd3;gap:24px}

/* back */
.back-hero{height:260px;background:var(--ink);display:flex;gap:18px;padding:26px 40px}
.back-hero__photo{width:300px;background:linear-gradient(150deg,#6f7d86 0%,#2f3a42 100%)}
.back-hero__drawing{flex:1;background:linear-gradient(150deg,#e7e9ec 0%,#b8bdc3 100%)}
.process-band{background:var(--green);color:#fff;padding:18px 40px}
.process-band h1{font-size:19px;font-weight:800;letter-spacing:.3px}
.process-band p{font-size:11.5px;margin-top:5px;font-weight:600}
.steps{list-style:none;padding:28px 40px 0 40px;position:relative}
.steps::before{content:"";position:absolute;left:60px;top:40px;bottom:30px;width:2px;background:var(--green-light)}
.step{display:flex;gap:22px;padding-bottom:24px;position:relative}
.step__num{width:42px;height:42px;border-radius:50%;background:var(--ink);color:#fff;font-family:"Montserrat",sans-serif;font-weight:800;font-size:16px;display:flex;align-items:center;justify-content:center;flex:none;border:3px solid var(--green)}
.step h3{font-size:13px;font-weight:700;color:var(--ink);letter-spacing:.4px}
.step p{font-size:11px;line-height:1.6;margin-top:4px}
.back-foot{position:absolute;bottom:0;left:0;right:0;height:60px;background:var(--green);color:#fff;display:flex;align-items:center;justify-content:space-between;padding:0 40px;font-family:"Montserrat",sans-serif;font-weight:600;font-size:12px}
</style>
</head>
<body>

<section class="page page--front">
  <header class="hero">
    <div class="hero__brand">
      <div class="brand"><span class="brand__dot"></span>VOLTA KADE</div>
      <div class="brand__sub">ELEKTRISCH VAREN</div>
    </div>
    <div class="hero__photo" role="img" aria-label="Foto van een elektrische sloep in de grachten bij het wateroppervlak"></div>
  </header>
  <div class="about-band">
    <h1>OVER VOLTA KADE</h1>
    <p>ELEKTRISCH VAREN</p>
  </div>
  <div class="who">
    <h2>WIE WIJ ZIJN</h2>
    <p>Wij bouwen elke boot van 4 tot 10 meter om naar elektrische aandrijving. Niet de goedkoopste, wel de beste, met alleen de beste materialen.</p>
  </div>
  <div class="front-body">
    <aside class="benefits">
      <h2>ONZE VOORDELEN</h2>
      <ul>
        <li><svg width="20" height="20" viewBox="0 0 20 20"><circle cx="10" cy="10" r="9" fill="none" stroke="#9bcb3c" stroke-width="2"/><path d="M6 10l3 3 5-6" fill="none" stroke="#9bcb3c" stroke-width="2"/></svg>Geruisloos varen</li>
        <li><svg width="20" height="20" viewBox="0 0 20 20"><circle cx="10" cy="10" r="9" fill="none" stroke="#9bcb3c" stroke-width="2"/><path d="M6 10l3 3 5-6" fill="none" stroke="#9bcb3c" stroke-width="2"/></svg>Geen uitlaatgassen of geur</li>
        <li><svg width="20" height="20" viewBox="0 0 20 20"><circle cx="10" cy="10" r="9" fill="none" stroke="#9bcb3c" stroke-width="2"/><path d="M6 10l3 3 5-6" fill="none" stroke="#9bcb3c" stroke-width="2"/></svg>Goedkoop in gebruik</li>
        <li><svg width="20" height="20" viewBox="0 0 20 20"><circle cx="10" cy="10" r="9" fill="none" stroke="#9bcb3c" stroke-width="2"/><path d="M6 10l3 3 5-6" fill="none" stroke="#9bcb3c" stroke-width="2"/></svg>Milieuvriendelijk</li>
        <li><svg width="20" height="20" viewBox="0 0 20 20"><circle cx="10" cy="10" r="9" fill="none" stroke="#9bcb3c" stroke-width="2"/><path d="M6 10l3 3 5-6" fill="none" stroke="#9bcb3c" stroke-width="2"/></svg>Verplicht in steeds meer gebieden</li>
        <li><svg width="20" height="20" viewBox="0 0 20 20"><circle cx="10" cy="10" r="9" fill="none" stroke="#9bcb3c" stroke-width="2"/><path d="M6 10l3 3 5-6" fill="none" stroke="#9bcb3c" stroke-width="2"/></svg>Geen onderhoud</li>
        <li><svg width="20" height="20" viewBox="0 0 20 20"><circle cx="10" cy="10" r="9" fill="none" stroke="#9bcb3c" stroke-width="2"/><path d="M6 10l3 3 5-6" fill="none" stroke="#9bcb3c" stroke-width="2"/></svg>Meer vaarplezier</li>
      </ul>
      <div class="benefits__photo" role="img" aria-label="Foto van een omgebouwde rondvaartboot aan de kade"></div>
      <div class="web-btn">www.volta-kade.nl</div>
    </aside>
    <div class="pricing">
      <h2>PRIJZEN VOOR HET OMBOUWEN</h2>
      <p class="pricing__intro">Elke ombouw is maatwerk. Hieronder vindt u een indicatie van de prijzen per type motor. Neem contact op voor een vrijblijvende offerte voor uw boot.</p>
      <div class="price-block">
        <h3>INBOARD<span>30 – 50 pk</span></h3>
        <ul><li>Elektromotor</li><li>Accupakket</li><li>Montage en test</li></ul>
        <div class="price-tag">v.a. € 9.500</div>
      </div>
      <div class="price-block">
        <h3>INBOARD<span>50 – 80 pk</span></h3>
        <ul><li>Elektromotor</li><li>Groot accupakket</li><li>Montage en test</li></ul>
        <div class="price-tag">v.a. € 14.500</div>
      </div>
      <div class="price-block">
        <h3>OUTBOARD<span>1 – 20 pk</span></h3>
        <ul><li>Buitenboordmotor</li><li>Lader en accu</li></ul>
        <div class="price-tag">v.a. € 1.800</div>
      </div>
      <div class="price-block">
        <h3>OUTBOARD<span>20 – 200 pk</span></h3>
        <ul><li>Buitenboordmotor</li><li>Accupakket</li><li>Installatie</li></ul>
        <div class="price-tag">v.a. € 6.900</div>
      </div>
    </div>
  </div>
  <footer class="front-foot"><span>www.volta-kade.nl</span><span>info@volta-kade.nl</span><span>020 555 0142</span></footer>
</section>

<section class="page page--back">
  <div class="back-hero">
    <div class="back-hero__photo" role="img" aria-label="Foto van boten in de haven"></div>
    <div class="back-hero__drawing" role="img" aria-label="Technische tekening van een elektromotor"></div>
  </div>
  <div class="process-band">
    <h1>HOE GAAT DE ELEKTRISCHE OMBOUW VAN UW BOOT IN ZIJN WERK?</h1>
    <p>Van eerste kennismaking tot proefvaart, in vijf duidelijke stappen.</p>
  </div>
  <ol class="steps">
    <li class="step"><div class="step__num">1</div><div><h3>KENNISMAKING</h3><p>We bespreken uw wensen, uw boot en het gewenste vaargebied, bij u aan de kade of bij ons op de werf.</p></div></li>
    <li class="step"><div class="step__num">2</div><div><h3>INSPECTIE EN OFFERTE</h3><p>We inspecteren de boot en maken een heldere offerte met motor, accu's en planning, zonder verrassingen.</p></div></li>
    <li class="step"><div class="step__num">3</div><div><h3>DEMONTAGE</h3><p>De dieselmotor, tank en leidingen worden netjes verwijderd en de motorruimte wordt gereinigd.</p></div></li>
    <li class="step"><div class="step__num">4</div><div><h3>INBOUW</h3><p>We plaatsen de elektromotor, het accupakket en de bediening met alleen de beste materialen.</p></div></li>
    <li class="step"><div class="step__num">5</div><div><h3>PROEFVAART EN OPLEVERING</h3><p>Samen maken we een proefvaart en leggen we alles uit. Daarna vaart u stil en schoon weg.</p></div></li>
  </ol>
  <footer class="back-foot"><span>Kadeweg 12, Amsterdam</span><span>020 555 0142</span><span>www.volta-kade.nl</span></footer>
</section>

</body>
</html>
```